Antigen Preservation Bureau

The company will provide a contract research services to stabilize various viruses, viral vectors, and vaccines. It may offer some licensing opportunities for stabilizing technologies. Main area of applications are pharmaceutical, therapeutic, and vaccination field. The company aspires to develop room temperature vaccines for global distribution beyond the current cold chain.

Target Market(s)

pharmaceutical, therapeutic and vaccination fields

Coding

Coded - Design and coding required

Number of Pages Required

4 page

Requirements
Must have
• Incorporate a APB logo, attached at the bottom, on the Web page

```html
<!DOCTYPE html>
<html lang="en">
<head>
<meta charset="utf-8">
<title>Antigen Preservation Bureau</title>
<link rel="stylesheet" href="https://fonts.googleapis.com/css2?family=Poppins:wght@400;500;600;700&family=Roboto:wght@400;500;700&display=swap">
<style>
:root{
  --coral:#f0555a;
  --teal:#4fc1bc;
  --ink:#1e2b33;
  --body:#6f7679;
  --muted:#9aa0a3;
  --line:#e6e8e9;
  --footer:#121212;
  --white:#ffffff;
}
*{margin:0;padding:0;box-sizing:border-box}
html,body{width:1200px;height:2835px;overflow:hidden}
body{position:relative;background:var(--white);font-family:'Roboto',sans-serif;color:var(--body)}
.abs{position:absolute}
h1,h2,h3,h4{font-family:'Poppins',sans-serif;color:var(--ink)}
.btn{display:inline-block;background:var(--coral);color:var(--white);font-family:'Poppins',sans-serif;font-weight:600;font-size:9px;letter-spacing:.5px;text-transform:uppercase;padding:8px 16px;border-radius:2px}
.btn.light{background:var(--white);color:var(--teal)}
.rule{width:30px;height:2px;background:var(--coral);margin:10px auto 0}
.section-title{position:absolute;left:0;width:1200px;text-align:center;font-size:23px;font-weight:600}
.section-title.upper{text-transform:uppercase}

/* header */
.topbar{left:0;top:0;width:1200px;height:47px}
.brand{left:274px;top:12px;display:flex;align-items:center;gap:8px}
.brand .mark{width:22px;height:22px;border-radius:50%;background:var(--coral);flex:none}
.brand .name{font-family:'Poppins',sans-serif;font-weight:700;font-size:11px;color:var(--teal);letter-spacing:.3px;line-height:22px;white-space:nowrap;text-transform:uppercase}
.contact{top:11px;display:flex;gap:8px;align-items:center;font-size:8.5px;line-height:1.35}
.contact svg{width:12px;height:12px}
.contact small{display:block;color:var(--muted);font-size:8px}
.contact span{color:var(--ink);white-space:nowrap}

.navbar{left:0;top:47px;width:1200px;height:34px;background:var(--teal)}
.nav{left:274px;top:0;display:flex;height:34px}
.nav a{display:block;line-height:34px;padding:0 14px;color:var(--white);font-family:'Poppins',sans-serif;font-size:9px;font-weight:500;text-transform:uppercase;text-decoration:none;margin-right:6px}
.nav a.active{background:var(--coral)}
.socials{display:flex;gap:5px}
.socials i{display:block;width:18px;height:18px;border-radius:50%;background:var(--white)}
.navbar .socials{position:absolute;left:834px;top:8px}

/* hero */
.hero{left:0;top:81px;width:1200px;height:444px;background:linear-gradient(120deg,#46525a 0%,#8a979d 40%,#cdd6da 60%,#6d7a80 100%)}
.hero-card{left:274px;top:102px;width:283px;height:242px;background:var(--white);padding:34px 34px;box-shadow:0 4px 18px rgba(0,0,0,.2)}
.hero-card h1{font-size:20px;font-weight:600;line-height:1.2;text-transform:uppercase}
.hero-card .rule{margin:14px 0 14px}
.hero-card p{font-size:9.5px;line-height:1.75;margin-bottom:16px}

/* services */
.services-title{top:575px}
.services{left:274px;top:646px;width:652px;display:flex;gap:14px}
.svc{width:208px;height:254px;border:1px solid var(--line);text-align:center;padding-top:30px;background:var(--white)}
.svc .icon{width:64px;height:64px;border-radius:50%;background:#f1f4f4;margin:0 auto 22px;display:flex;align-items:center;justify-content:center}
.svc h3{font-size:13px;font-weight:500;color:var(--teal);margin-bottom:10px}
.svc p{font-size:8.5px;line-height:1.7;padding:0 20px;margin-bottom:16px}
.svc.featured{background:var(--teal);border-color:var(--teal);box-shadow:0 6px 16px rgba(0,0,0,.15)}
.svc.featured .icon{background:var(--white)}
.svc.featured h3,.svc.featured p{color:var(--white)}

/* welcome */
.welcome{left:0;top:956px;width:1200px;height:400px;background:linear-gradient(90deg,#eef0f1,#f6f6f4 60%,#ecebe6)}
.welcome-img{left:0;top:0;width:500px;height:400px;background:radial-gradient(circle at 55% 55%,#ffffff 0%,#e3e7e8 55%,#cdd3d4 100%)}
.welcome-text{left:584px;top:54px;width:342px}
.welcome-text .eyebrow{font-size:9.5px;letter-spacing:2px;color:var(--coral);text-transform:uppercase}
.welcome-text h2{font-size:21px;font-weight:500;margin-top:4px}
.welcome-text .rule{margin:10px 0 14px}
.welcome-text p{font-size:8.5px;line-height:1.75;margin-bottom:12px}

/* staff */
.staff-title{top:1400px}
.staff{left:274px;top:1465px;width:652px;display:flex;gap:11px}
.member{width:155px;text-align:center}
.member .photo{height:157px;background:linear-gradient(160deg,#dfe9f2,#b9cad8)}
.member h4{font-size:12px;font-weight:500;margin-top:10px}
.member .role{font-size:7.5px;color:var(--muted);margin-top:2px}
.member p{font-size:8px;line-height:1.6;margin-top:8px;padding:0 8px}
.member .icons{display:flex;justify-content:center;gap:7px;margin-top:10px}
.member .icons i{width:8px;height:8px;border-radius:50%;background:#8d9497}

/* testimonials */
.testimonials{left:0;top:1771px;width:1200px;height:395px;background:linear-gradient(100deg,#ef5c5d 0%,#dd8a87 40%,#8cb6b3 65%,#4dbdb6 100%);color:var(--white);text-align:center}
.testimonials .eyebrow{position:absolute;left:0;top:55px;width:1200px;font-size:9.5px;letter-spacing:2px;text-transform:uppercase}
.testimonials h2{position:absolute;left:0;top:68px;width:1200px;font-size:23px;font-weight:500;color:var(--white)}
.testimonials .quote{position:absolute;left:584px;top:136px}
.testimonials p{position:absolute;left:364px;top:192px;width:472px;font-size:9px;line-height:1.8}
.testimonials .avatar{position:absolute;left:575px;top:260px;width:50px;height:50px;border-radius:50%;background:#f3d7cf;border:3px solid var(--white)}
.testimonials .who{position:absolute;left:0;top:318px;width:1200px;font-family:'Poppins',sans-serif;font-size:10px;font-weight:500}
.testimonials .who small{display:block;font-size:7px;letter-spacing:1px;font-weight:400}
.arrow{position:absolute;top:182px}

/* news */
.news-title{top:2207px;font-weight:500}
.news-main{left:274px;top:2270px;width:322px;height:297px;background:linear-gradient(150deg,#cfd9de,#7e93a0 70%,#5f7482)}
.news-main .caption{position:absolute;left:10px;bottom:10px;width:302px;background:var(--white);padding:12px 12px}
.news-date{font-size:7.5px;color:var(--coral)}
.news-main h3{font-size:12px;font-weight:500;margin:3px 0 6px;white-space:nowrap}
.news-main p{font-size:8px;line-height:1.6}
.news-list{left:605px;top:2270px;width:321px;display:flex;flex-direction:column;gap:10px}
.news-item{display:flex;height:92px;border:1px solid var(--line)}
.news-item .thumb{width:111px;flex:none}
.news-item .body{padding:8px 10px}
.news-item h4{font-size:11px;font-weight:500;margin:3px 0 4px}
.news-item .mini{width:18px;height:2px;background:var(--coral);margin-bottom:5px}
.news-item p{font-size:7.5px;line-height:1.55}

/* footer */
.footer{left:0;top:2623px;width:1200px;height:170px;background:var(--footer);color:#b8bcbe}
.footer .brand{left:274px;top:34px}
.footer .about{position:absolute;left:274px;top:74px;width:180px;font-size:8px;line-height:1.7}
.footer h5{font-family:'Poppins',sans-serif;font-size:10px;font-weight:500;color:var(--white);text-transform:uppercase;margin-bottom:12px}
.fcol{position:absolute;top:50px;font-size:7.5px;line-height:1.9;text-transform:uppercase}
.fcol .cols{display:flex;gap:40px}
.newsletter input{display:block;width:134px;height:22px;border:0;background:var(--white)}
.newsletter .btn{margin-top:8px;padding:6px 10px;font-size:8px}
.bottombar{left:0;top:2793px;width:1200px;height:42px;background:var(--coral);color:var(--white)}
.bottombar .copy{position:absolute;left:274px;top:15px;font-size:8px}
.bottombar .socials{position:absolute;left:834px;top:12px}
</style>
</head>
<body>

<header class="abs topbar">
  <div class="abs brand"><span class="mark"></span><span class="name">Antigen Preservation Bureau</span></div>
  <div class="abs contact" style="left:548px">
    <svg viewBox="0 0 12 12"><rect x="1" y="2.5" width="10" height="7" rx="1" fill="#f0555a"/><path d="M1.5 3l4.5 3.5L10.5 3" stroke="#fff" fill="none" stroke-width="1"/></svg>
    <div><small>Email us</small><span>hello@apbureau.org</span></div>
  </div>
  <div class="abs contact" style="left:686px">
    <svg viewBox="0 0 12 12"><path d="M3 1.5l2 2.5-1.2 1.2a6 6 0 003 3L8 7l2.5 2-1 1.5C5.5 10.5 1.5 6.5 1.5 2.5z" fill="#f0555a"/></svg>
    <div><small>Call us</small><span>1-800-555-0147</span></div>
  </div>
  <div class="abs contact" style="left:803px">
    <svg viewBox="0 0 12 12"><path d="M6 1a3.5 3.5 0 00-3.5 3.5C2.5 7.5 6 11 6 11s3.5-3.5 3.5-6.5A3.5 3.5 0 006 1z" fill="#f0555a"/><circle cx="6" cy="4.5" r="1.2" fill="#fff"/></svg>
    <div><small>Visit us</small><span>48 Harbor Lane, Suite 210</span></div>
  </div>
</header>

<nav class="abs navbar">
  <div class="abs nav">
    <a class="active">Home</a><a>About us</a><a>Services</a><a>Testimonials</a><a>Blog</a><a>Contact us</a>
  </div>
  <div class="socials"><i></i><i></i><i></i><i></i></div>
</nav>

<section class="abs hero" role="img" aria-label="Photo of scientists in lab coats working in a laboratory">
  <div class="abs hero-card" role="group" aria-label="Intro">
    <h1>Lorem ipsum dolor sit adipiscing</h1>
    <div class="rule"></div>
    <p>Maecenas hendrerit enim in orci placerat blandit. Quisque nisl dui, laoreet quis auctor tempus, maximus sit amet tortor. Duis scelerisque dolor.</p>
    <span class="btn">Read more</span>
  </div>
</section>

<h2 class="section-title upper services-title">Our Services<div class="rule"></div></h2>
<div class="abs services">
  <div class="svc">
    <div class="icon"><svg width="30" height="30" viewBox="0 0 30 30"><rect x="4" y="10" width="18" height="10" rx="5" fill="#4fc1bc"/><circle cx="21" cy="19" r="6" fill="#f0555a"/></svg></div>
    <h3>Pharmaceutical</h3>
    <p>Morbi semper, erat id ultrices interdum, magna ante iaculis magna, eu ornare velit metus quis velit. Maecenas gravida.</p>
    <span class="btn">Read more</span>
  </div>
  <div class="svc featured">
    <div class="icon"><svg width="30" height="30" viewBox="0 0 30 30"><path d="M5 15h20a10 10 0 01-20 0z" fill="#4fc1bc"/><circle cx="15" cy="9" r="3" fill="#4fc1bc"/><circle cx="10" cy="11" r="2" fill="#4fc1bc"/><circle cx="20" cy="11" r="2" fill="#4fc1bc"/></svg></div>
    <h3>Therapeutic</h3>
    <p>Morbi semper, erat id ultrices interdum, magna ante iaculis magna, eu ornare velit metus quis velit. Maecenas gravida.</p>
    <span class="btn light">Read more</span>
  </div>
  <div class="svc">
    <div class="icon"><svg width="30" height="30" viewBox="0 0 30 30"><path d="M8 22L20 10" stroke="#4fc1bc" stroke-width="5" stroke-linecap="round"/><path d="M20 10l5-5M5 25l3-3" stroke="#f0555a" stroke-width="2" stroke-linecap="round"/></svg></div>
    <h3>Vaccination</h3>
    <p>Morbi semper, erat id ultrices interdum, magna ante iaculis magna, eu ornare velit metus quis velit. Maecenas gravida.</p>
    <span class="btn">Read more</span>
  </div>
</div>

<section class="abs welcome">
  <div class="abs welcome-img" role="img" aria-label="Photo of laboratory glassware with a mortar, pestle and green leaves"></div>
  <div class="abs welcome-text">
    <div class="eyebrow">Welcome to</div>
    <h2>Antigen Preservation Bureau</h2>
    <div class="rule"></div>
    <p>Lorem ipsum dolor sit amet, consectetur adipiscing elit. Sed laoreet tincidunt iaculis. Praesent lacus turpis, venenatis ac euismod ac, ultrices eu elit. Pellentesque scelerisque congue metus, vel malesuada ex laoreet non. Aliquam erat volutpat. Aliquam diam sem, consequat sit amet arcu non, egestas hendrerit erat. Cras convallis, est ultricies consectetur congue, justo justo elementum risus, a rutrum sapien odio sit amet purus.</p>
    <p>Curabitur egestas neque sit amet eros iaculis volutpat. In interdum luctus lectus eu tempus. Nam lacinia diam sed viverra viverra. Mauris tellus sapien, malesuada eget euismod ac, dapibus in orci. Morbi in molestie ligula. Nunc sed purus in orci interdum ornare. Nullam elementum et massa ut ultrices.</p>
    <span class="btn">Read more</span>
  </div>
</section>

<h2 class="section-title upper staff-title">Our Talented Staff<div class="rule"></div></h2>
<div class="abs staff">
  <div class="member"><div class="photo" role="img" aria-label="Portrait photo of a staff member"></div><h4>Marek Halden</h4><div class="role">Rehabilitation Therapy</div><p>Praesent augue sem, euismod sit amet porta vitae, varius nunc.</p><div class="icons"><i></i><i></i><i></i><i></i></div></div>
  <div class="member"><div class="photo" role="img" aria-label="Portrait photo of a staff member"></div><h4>Marek Halden</h4><div class="role">Rehabilitation Therapy</div><p>Praesent augue sem, euismod sit amet porta vitae, varius nunc.</p><div class="icons"><i></i><i></i><i></i><i></i></div></div>
  <div class="member"><div class="photo" role="img" aria-label="Portrait photo of a staff member"></div><h4>Marek Halden</h4><div class="role">Rehabilitation Therapy</div><p>Praesent augue sem, euismod sit amet porta vitae, varius nunc.</p><div class="icons"><i></i><i></i><i></i><i></i></div></div>
  <div class="member"><div class="photo" role="img" aria-label="Portrait photo of a staff member"></div><h4>Marek Halden</h4><div class="role">Rehabilitation Therapy</div><p>Praesent augue sem, euismod sit amet porta vitae, varius nunc.</p><div class="icons"><i></i><i></i><i></i><i></i></div></div>
</div>

<section class="abs testimonials" role="img" aria-label="Photo of a patient receiving care, tinted coral to teal">
  <div class="eyebrow">What the say?</div>
  <h2>Client Testimonials</h2>
  <svg class="quote" width="32" height="28" viewBox="0 0 32 28"><path d="M2 14C2 7 6 3 12 2v5c-3 1-4 3-4 6h5v13H2zM19 14c0-7 4-11 10-12v5c-3 1-4 3-4 6h5v13H19z" fill="#fff"/></svg>
  <svg class="arrow" style="left:272px" width="24" height="14" viewBox="0 0 24 14"><path d="M23 7H2M8 1L2 7l6 6" stroke="#fff" stroke-width="1.5" fill="none"/></svg>
  <svg class="arrow" style="left:904px" width="24" height="14" viewBox="0 0 24 14"><path d="M1 7h21M16 1l6 6-6 6" stroke="#fff" stroke-width="1.5" fill="none"/></svg>
  <p>Lorem ipsum dolor sit amet, consectetur adipiscing elit. Sed laoreet tincidunt iaculis. Praesent lacus turpis, venenatis ac euismod ac, ultrices eu elit. Pellentesque scelerisque congue metus, vel malesuada ex laoreet non. Aliquam erat volutpat. Aliquam diam sem, consequat sit amet arcu non, egestas hendrerit erat.</p>
  <div class="avatar" role="img" aria-label="Customer portrait"></div>
  <div class="who">Lena Morrow<small>CUSTOMER</small></div>
</section>

<h2 class="section-title news-title">Latest News<div class="rule"></div></h2>
<div class="abs news-main" role="img" aria-label="Photo of a scientist using a microscope">
  <div class="caption">
    <div class="news-date">September 28-29</div>
    <h3>Praesent dictum at quam condimentum</h3>
    <p>Lorem ipsum dolor sit amet, consectetur adipiscing elit, sed diam nonummy nibh euismod tincidunt ut laoreet dolore magna ut wisi enim.</p>
  </div>
</div>
<div class="abs news-list">
  <div class="news-item"><div class="thumb" role="img" aria-label="Photo of a researcher in a lab" style="background:linear-gradient(150deg,#e9eef0,#b6c6cc)"></div><div class="body"><div class="news-date">September 28-29</div><h4>Praesent dictum at quam</h4><div class="mini"></div><p>Lorem ipsum dolor sit amet, consectetur adipiscing elit. Sed laoreet tincidunt iaculis. Praesent</p></div></div>
  <div class="news-item"><div class="thumb" role="img" aria-label="Photo of assorted pills" style="background:linear-gradient(150deg,#8fd3e0,#e8b06a)"></div><div class="body"><div class="news-date">September 28-29</div><h4>Condimentum laoreet</h4><div class="mini"></div><p>Lorem ipsum dolor sit amet, consectetur adipiscing elit. Sed laoreet tincidunt iaculis. Praesent</p></div></div>
  <div class="news-item"><div class="thumb" role="img" aria-label="Photo of medical staff at work" style="background:linear-gradient(150deg,#9fb3c4,#3e5d7e)"></div><div class="body"><div class="news-date">September 28-29</div><h4>Condimentum laoreet</h4><div class="mini"></div><p>Lorem ipsum dolor sit amet, consectetur adipiscing elit. Sed laoreet tincidunt iaculis. Praesent</p></div></div>
</div>

<footer class="abs footer">
  <div class="abs brand"><span class="mark"></span><span class="name">Antigen Preservation Bureau</span></div>
  <p class="about">Lorem ipsum dolor sit amet, consectetur adipiscing elit. Sed laoreet tincidunt iaculis. Praesent lacus turpis, venenatis ac euismod ac, ultrices eu elit. Pellentesque scelerisque.</p>
  <div class="fcol" style="left:493px"><h5>Quick Links</h5><div class="cols"><div>Home<br>About us<br>Services</div><div>Testimonials<br>Blog<br>Contact us</div></div></div>
  <div class="fcol" style="left:665px"><h5>Our Services</h5>Pharmaceutical<br>Therapeutic<br>Vaccination</div>
  <div class="fcol newsletter" style="left:792px"><h5>Newsletter</h5><input type="text" aria-label="Email address"><span class="btn">Subscribe</span></div>
</footer>
<div class="abs bottombar">
  <div class="copy">Copyright © 2019 Antigen Preservation Bureau. All Rights Reserved.</div>
  <div class="socials"><i></i><i></i><i></i><i></i></div>
</div>

</body>
</html>
```